The Amp Fellow

need a business card for a dj and sound equipment hire(rentals) business based in Melbourne. i have attached a current card get an idea. card needs to be unique professional looking.

ps.this card is not for a DJ. it's a rental business of dj equipment and pa systems.

Industry/Entity Type

Business

Font styles to use
Sans Serif
Script

Requirements
Must have
• Business Name: THE AMP FELLOW
Contact Person: RAVINDU PERERALA
Mobile: 047 BASSY 82
Email: RAVINDU@THEAMPFELLOW.COM.AU
Website: WWW.THEAMPFELLOW.COM.AU
Facebook: WWW.FACEBOOK.CM/THEAMPFELLOW.COM.AU

```html
<!DOCTYPE html>
<html lang="en">
<head>
<meta charset="utf-8">
<title>The Amp Fellow – Business Card</title>
<link rel="stylesheet" href="https://fonts.googleapis.com/css2?family=Open+Sans:ital,wght@0,400;0,700;1,400&display=swap">
<style>
  :root {
    --yellow: #ecd02a;
    --teal: #1f7487;
    --ink: #111111;
    --photo-light: #e4e2dc;
    --photo-mid: #c9c4b8;
    --photo-dark: #9c978c;
  }
  html, body {
    margin: 0;
    padding: 0;
    overflow: hidden;
    background: #ffffff;
  }
  .card {
    position: relative;
    width: 1200px;
    height: 741px;
    overflow: hidden;
    background: var(--yellow);
    font-family: "Open Sans", sans-serif;
  }
  .card-shapes {
    position: absolute;
    inset: 0;
  }
  .shape-teal { fill: var(--teal); }
  .guide-line { stroke: var(--teal); stroke-width: 1; }
  .contact-ring { fill: none; stroke: var(--teal); stroke-width: 3; }

  .equipment-photo {
    position: absolute;
    left: 720px;
    top: 181px;
    width: 480px;
    height: 249px;
    background: linear-gradient(120deg, var(--photo-light) 0%, var(--photo-mid) 55%, var(--photo-dark) 100%);
  }

  .contact-name,
  .contact-mobile,
  .brand-name,
  .brand-tagline,
  .contact-link {
    position: absolute;
    margin: 0;
    white-space: nowrap;
  }
  .contact-name {
    left: 106px;
    top: 271px;
    font-size: 49px;
    font-weight: 700;
    color: var(--ink);
    letter-spacing: 0.5px;
  }
  .contact-mobile {
    left: 106px;
    top: 329px;
    font-size: 36px;
    font-weight: 700;
    color: var(--ink);
  }
  .brand-name {
    left: 728px;
    top: 271px;
    font-size: 58px;
    font-weight: 700;
    color: var(--teal);
    line-height: 1;
    letter-spacing: -1px;
  }
  .brand-tagline {
    left: 722px;
    top: 323px;
    font-size: 28px;
    font-style: italic;
    color: var(--ink);
  }
  .contact-link {
    top: 610px;
    font-size: 20.5px;
    color: var(--ink);
  }
  .contact-email { left: 65px; }
  .contact-web { left: 426px; }
  .contact-social { left: 748px; }
</style>
</head>
<body>
<div class="card">
  <svg class="card-shapes" width="1200" height="741" viewBox="0 0 1200 741" aria-hidden="true">
    <line class="guide-line" x1="37" y1="0" x2="37" y2="741"/>
    <line class="guide-line" x1="396" y1="0" x2="396" y2="741"/>
    <line class="guide-line" x1="719" y1="0" x2="719" y2="741"/>

    <rect class="shape-teal" x="636" y="0" width="84" height="181"/>
    <rect class="shape-teal" x="6" y="150" width="714" height="31"/>
    <rect class="shape-teal" x="0" y="181" width="720" height="249"/>
    <rect class="shape-teal" x="0" y="430" width="24" height="87"/>
    <rect class="shape-teal" x="0" y="489" width="653" height="28"/>

    <rect class="shape-teal" x="488" y="479" width="712" height="17"/>
    <rect class="shape-teal" x="1117" y="496" width="83" height="201"/>
    <rect class="shape-teal" x="488" y="697" width="712" height="31"/>

    <circle class="contact-ring" cx="37" cy="625" r="20"/>
    <circle class="contact-ring" cx="396" cy="625" r="20"/>
    <circle class="contact-ring" cx="720" cy="625" r="20"/>
  </svg>

  <div class="equipment-photo" role="img" aria-label="Close-up photo of a sound mixing desk with knobs and a microphone grille"></div>

  <h1 class="contact-name">RAVINDU PERERALA</h1>
  <p class="contact-mobile">047 BASSY 82</p>

  <p class="brand-name">the amp fellow</p>
  <p class="brand-tagline">sound equipment hire</p>

  <p class="contact-link contact-email">ravindu@theampfellow.com.au</p>
  <p class="contact-link contact-web">www.theampfellow.com.au</p>
  <p class="contact-link contact-social">www.socialpage.cm/theampfellow.com.au</p>
</div>
</body>
</html>
```